Brochure Design Project for a Psychotherapy Private Practice.

I am a psychologist and I own my private practice. I need brochures to market to doctors and healthcare providers so that they understand the psychotherapy services that I deliver. I also want the brochures to be informative to potential patients. I have included a word document that details the services that I offer.
Target Market(s)
Referring healthcare providers (medical doctors, naturopaths, physician assistants, nurse practitioners) and patients who are seeking psychotherapy.
Industry/Entity Type
Healthcare
Colors
Designer to choose colors to be used in the design.
Look and feel

```html
<!DOCTYPE html>
<html lang="en">
<head>
<meta charset="utf-8">
<title>Harbor Light Psychological Services – Brochure</title>
<link rel="stylesheet" href="https://fonts.googleapis.com/css2?family=Quicksand:wght@300;400;500&family=Nunito:ital,wght@0,400;0,900;1,400&family=Oswald:wght@300;400;700&display=swap">
<style>
  :root{
    --peach:#fde4cf;
    --orange:#f0692a;
    --teal:#2e5a62;
    --mist:#dfe5e7;
    --blue:#1574c2;
    --ink:#2f3b3e;
    --slate:#4d6a70;
    --white:#ffffff;
  }
  *{box-sizing:border-box;margin:0;padding:0}
  html,body{width:1200px;height:858px;overflow:hidden;background:var(--white)}
  .brochure{position:relative;width:1200px;height:858px;overflow:hidden;font-family:"Quicksand",sans-serif}

  /* Left panel: therapies */
  .panel-therapies{position:absolute;left:0;top:0;width:404px;height:804px;background:var(--peach);padding:27px 19px 0 32px;color:var(--ink)}
  .panel-therapies p{font-size:12.3px;line-height:15.45px;text-align:justify;font-weight:500}
  .panel-therapies h3{font-family:"Nunito",sans-serif;font-weight:900;color:var(--orange);font-size:14.6px;line-height:18px;margin:3px 0 3px}

  /* Middle panel */
  .panel-start{position:absolute;left:404px;top:0;width:392px;height:858px;background:var(--teal)}
  .panel-start .title{font-family:"Nunito",sans-serif;font-weight:900;color:var(--white);font-size:23px;text-align:center;padding-top:25px;line-height:30px}
  .steps{position:absolute;left:0;top:58px;width:392px;height:320px;background:var(--mist);padding:2px 19px 0 15px}
  .steps h2{font-family:"Nunito",sans-serif;font-weight:900;color:var(--teal);font-size:24px;line-height:26px}
  .steps p{font-size:12.7px;line-height:15.4px;color:var(--slate);text-align:justify;font-weight:500;margin-bottom:6px}
  .portrait{position:absolute;left:17px;top:397px;width:142px;height:148px;background:linear-gradient(160deg,#8a8f7a,#5c4638 55%,#2c3444)}
  .bio{position:absolute;left:17px;top:397px;width:361px;font-family:"Nunito",sans-serif;font-style:italic;color:var(--white);font-size:12.8px;line-height:15.4px;text-align:justify}
  .bio .float{float:left;width:150px;height:148px}
  .brand-box{position:absolute;left:0;top:672px;width:392px;height:128px;background:var(--white);display:flex;align-items:center;justify-content:center;gap:14px}
  .brand-mark{width:34px;height:34px;border-radius:50%;background:var(--teal)}
  .brand-name{font-family:"Quicksand",sans-serif;font-weight:300;color:#6a7b7f;font-size:25px;line-height:29px}
  .site{position:absolute;left:0;top:812px;width:392px;text-align:center;color:var(--white);font-family:"Nunito",sans-serif;font-weight:900;font-size:13.8px;letter-spacing:.2px}

  /* Right panel: cover */
  .panel-cover{position:absolute;left:796px;top:0;width:404px;height:858px}
  .panel-cover svg{position:absolute;left:0;top:0}
  .cover-brand{position:absolute;left:18px;top:40px;display:flex;align-items:center;gap:22px}
  .cover-brand .brand-mark{width:48px;height:48px;background:transparent;border:3px solid var(--white)}
  .cover-brand .brand-name{color:var(--white);font-size:28px;line-height:33px}
  .headline{position:absolute;left:0;top:0;width:404px;height:858px;font-family:"Oswald",sans-serif;color:var(--white)}
  .headline span{position:absolute;white-space:nowrap;line-height:1}
  .hl-bold{font-weight:700}
  .hl-light{font-weight:300}
</style>
</head>
<body>
<div class="brochure">

  <section class="panel-therapies">
    <p>behaviors. Clients learn how to reframe maladaptive thoughts and implement effective solutions to address life's problems. Through the use of skill building and cognitive restructuring, CBT promotes long-term results that can improve your overall quality of life.</p>
    <h3>Dialectical Behavior Therapy (DBT)</h3>
    <p>Dialectical Behavior Therapy, developed by Miriam L. Hartwell, ABPP, Ph.D., is evidenced based, cognitive behavioral treatment which focuses on accepting clients as they are while also acknowledging they need to change in order to reach their goals. A key component of dialectical behavior therapy is skills training, which includes the teaching and application of skills in mindfulness, emotion regulation, interpersonal effectiveness, and distress tolerance. Though DBT was initially designed to treat Borderline Personality Disorder, research demonstrates efficacy in the treatment of many disorders including depression and anxiety.</p>
    <h3>Imagery Rehearsal Therapy (IRT)</h3>
    <p>Imagery Rehearsal Therapy, researched by Bernard Kessler, M.D., is a cognitive behavioral treatment for reducing the number and intensity of nightmares among people with posttraumatic stress disorder (PTSD). This treatment has been modified by Ronald Ferrante, MD to specifically treat nightmares and flashbacks experienced by victims of assault (physical or sexual) or witnesses to traumatic events. Modified IRT is short-term and does not required clients to relive the traumatic event via prolonged exposure therapy.</p>
    <h3>Interpersonal Psychotherapy (IPT)</h3>
    <p>Interpersonal Psychotherapy is a time-limited, attachment-focused therapy that focuses on resolving current difficulties and improving interpersonal relationships. Some of these difficulties may include the death of a loved one or unresolved grief, the beginning or ending of a relationship or marriage, the diagnosis of a disease, struggles in relationships related to role disputes, and/or the absence of a major life event.</p>
    <h3>Mindfulness-Based Stress Reduction (MBSR)</h3>
    <p>Mindfulness-based Stress Reduction was developed at the Northfield University Medical Center by Professor Joel Kaplan-Ross. The basic foundation of MBSR is to focus one's awareness in the present moment without judgment. Research currently supports the effectiveness of mindfulness-based practices to reduce symptoms of depression and anxiety, and contributes to stress reduction, relaxation, and improvement of overall quality of life.</p>
  </section>

  <section class="panel-start">
    <div class="title">Getting Started:</div>
    <div class="steps">
      <h2>Consultation</h2>
      <p>I offer a complimentary 30-minute consultation (on the phone), so you can get a sense of whether we are a good fit. It will also give me an opportunity to determine if I am the best therapist to be able to help you. In the event that we are not a good match, I can connect you with another practitioner to serve your needs.</p>
      <h2>Intake</h2>
      <p>During our first session, we will address your presenting problem(s) and collect a thorough background of your history, so that I can best understand your problem areas in the context of who you are. We will also conduct an assessment of your current symptoms, address provisional diagnoses (if applicable), discuss potential treatment goals, and develop a tentative treatment plan with recommendations for therapy duration and frequency.</p>
    </div>
    <div class="portrait" role="img" aria-label="Portrait photograph of the psychologist"></div>
    <p class="bio"><span class="float"></span>Dr. Varela graduated from the Westbrook State University and received her Doctoral degree in Clinical Psychology at the Pacific Institute of Professional Psychology, Bayview. She completed her predoctoral internship in behavioral medicine and rehabilitation psychology at the Eastport Veterans Healthcare System/Eastport Medical School and a postdoctoral fellowship at the Cognitive Intensive Outpatient Program, Ridgeview Hospital, Lakeside. Dr. Varela is a member of the National Psychological Society, Institute of Cognitive Therapy, and the Coastal Region Psychological Association.</p>
    <div class="brand-box">
      <span class="brand-mark"></span>
      <span class="brand-name">Harbor Light<br>Psychological<br>Services</span>
    </div>
    <div class="site">www.harborlightpsych.example</div>
  </section>

  <section class="panel-cover">
    <svg width="404" height="858" viewBox="0 0 404 858" aria-hidden="true">
      <defs>
        <linearGradient id="roomTone" x1="0" y1="0" x2="1" y2="1">
          <stop offset="0" stop-color="#e9e6e1"/>
          <stop offset="0.5" stop-color="#cfc9c2"/>
          <stop offset="0.75" stop-color="#1f2433"/>
          <stop offset="1" stop-color="#b9a58c"/>
        </linearGradient>
      </defs>
      <rect width="404" height="858" fill="#ffffff"/>
      <polygon points="0,0 404,0 404,72 0,200" fill="var(--teal)"/>
      <polygon points="0,204 404,76 404,544 0,672" fill="var(--blue)"/>
      <polygon points="0,680 404,552 404,858 0,858" fill="var(--teal)"/>
      <polygon points="0,686 404,558 404,858 0,858" fill="url(#roomTone)" role="img" aria-label="Photograph of a calm therapy room with a dark sofa, cushions and white shelving"/>
    </svg>
    <div class="cover-brand">
      <span class="brand-mark"></span>
      <span class="brand-name">Harbor Light<br>Psychological<br>Services</span>
    </div>
    <h1 class="headline">
      <span class="hl-bold" style="left:58px;top:200px;font-size:46px">Work</span>
      <span class="hl-bold" style="left:42px;top:232px;font-size:58px">together</span>
      <span class="hl-light" style="left:138px;top:290px;font-size:30px">to</span>
      <span class="hl-bold" style="left:76px;top:303px;font-size:52px">develop</span>
      <span class="hl-light" style="left:142px;top:353px;font-size:25px">a</span>
      <span class="hl-bold" style="left:104px;top:360px;font-size:54px">healthier</span>
      <span class="hl-light" style="left:196px;top:410px;font-size:36px">thought</span>
      <span class="hl-bold" style="left:92px;top:431px;font-size:52px">process</span>
      <span class="hl-light" style="left:214px;top:474px;font-size:32px">and</span>
      <span class="hl-bold" style="left:40px;top:490px;font-size:50px">effective coping</span>
      <span class="hl-bold" style="left:116px;top:536px;font-size:52px">skills,</span>
    </h1>
  </section>

</div>
</body>
</html>
```